Tellwick Asset Management - Corporate Letter Head Project

Looking for a classy design based on our current logo. Please find current logo source file in files. With our color scheme.

Target Market(s)

We're an investment firm, the letterhead needs to look professional and attractive to clients.

Industry/Entity Type

Hedgefund

Colors
0054AA
0677BA
7BADD7
CADEEF
E8F1F8

Requirements
Must have
• Our logo, address, phone number, and email

```html
<!DOCTYPE html>
<html lang="en">
<head>
<meta charset="utf-8">
<title>Tellwick Asset Management – Letterhead</title>
<link rel="stylesheet" href="https://fonts.googleapis.com/css2?family=Cinzel:wght@500&family=Montserrat:wght@400&display=swap">
<style>
  :root {
    --ink: #1b2847;
    --paper: #ffffff;
    --backdrop: #e9edf2;
    --edge: #d9dde3;
  }
  * { box-sizing: border-box; margin: 0; padding: 0; }
  html, body {
    width: 1200px;
    height: 1200px;
    overflow: hidden;
    background: var(--backdrop);
  }
  .canvas {
    width: 1200px;
    height: 1200px;
    display: flex;
    align-items: center;
    justify-content: center;
  }
  .letterhead {
    position: relative;
    width: 812px;
    height: 1148px;
    background: var(--paper);
    border: 1px solid var(--edge);
    box-shadow: 0 6px 22px rgba(27, 40, 71, 0.10);
  }
  .brand {
    position: absolute;
    left: 56px;
    top: 148px;
    display: flex;
    align-items: center;
    gap: 16px;
    color: var(--ink);
  }
  .brand-mark {
    width: 62px;
    height: 62px;
    border: 2px solid var(--ink);
  }
  .brand-name {
    font-family: "Cinzel", "Times New Roman", serif;
    font-weight: 500;
    line-height: 1;
    white-space: nowrap;
  }
  .brand-name-main {
    display: block;
    font-size: 31px;
    letter-spacing: 0.01em;
  }
  .brand-name-sub {
    display: block;
    margin-top: 3px;
    font-size: 12px;
    letter-spacing: 0.86em;
  }
  .contact {
    position: absolute;
    right: 64px;
    top: 52px;
    display: flex;
    gap: 20px;
    color: var(--ink);
    font-family: "Montserrat", Arial, sans-serif;
    font-style: normal;
    font-size: 14px;
    line-height: 1.3;
  }
  .contact-rule {
    width: 1px;
    background: var(--ink);
  }
  .contact-address { margin-bottom: 10px; }
  .contact-line {
    display: flex;
    align-items: center;
    gap: 6px;
  }
  .contact-line svg {
    width: 12px;
    height: 12px;
    fill: var(--ink);
    flex: none;
  }
</style>
</head>
<body>
  <main class="canvas">
    <article class="letterhead">
      <header>
        <div class="brand">
          <div class="brand-mark" aria-hidden="true"></div>
          <p class="brand-name">
            <span class="brand-name-main">Tellwick Asset</span>
            <span class="brand-name-sub">Management</span>
          </p>
        </div>

        <address class="contact">
          <div class="contact-rule" aria-hidden="true"></div>
          <div class="contact-details">
            <p class="contact-address">Your address, City<br>State, Zip 123400</p>
            <p class="contact-line">
              <svg viewBox="0 0 24 24" aria-hidden="true"><path d="M3 9c0-3 4-5 9-5s9 2 9 5v2h-5V9c0-1-2-1.5-4-1.5S8 8 8 9v2H3z M6 13h12l2 7H4z"/></svg>
              <span>123 456 789 000</span>
            </p>
            <p class="contact-line">
              <svg viewBox="0 0 24 24" aria-hidden="true"><path d="M2 5h20v14H2z M3.5 6.5 12 13l8.5-6.5" stroke="#fff" stroke-width="1.6"/></svg>
              <span>info@tellwickam.com</span>
            </p>
          </div>
        </address>
      </header>
    </article>
  </main>
</body>
</html>
```